Social Media Infographic for White Paper

Am working on a white paper on social media use by C-Suite Executives, and hope to include some infographics. I would like some help designing the first infographic.

The master bit of information is that "66% of C-Suite Executives use social media for professional purpose."

Within that 66%
-70% post original content on a daily/weekly basis
-13% of professional users are lurkers
-40% plan to use social media even more in the future

After initial design will need to two versions of the infographic, one listing the source at the bottom in small print (Source: 2017 Venmoor Partners Executive Social Media Study), the other one with no source information.

Infographic design should be complimentary with my website: www.venmoorpartners.example, but use of green should be very limited, if at all.

Target Market(s)

New media, C-Suite Executives, Executive Coaches

Industry/Entity Type

Management Consulting

Font styles to use
Sans Serif

Requirements
Must have
• Infographic with data displayed in a easy to understand format that tells the story of C-Suite Executives that participate in social media for professional purposes.
Nice to have
• Complements website design - www.venmoor.example.
Should not have
• Limit use of green from website logo, which can be overpowering. Some is ok, but not too much

```html
<!DOCTYPE html>
<html lang="en">
<head>
<meta charset="utf-8">
<title>C-Suite Executives on Social Media</title>
<link rel="stylesheet" href="https://fonts.googleapis.com/css2?family=Montserrat:wght@500;600&family=Oswald:wght@600&display=swap">
<style>
  :root {
    --ink: #2b2c27;
    --stone: #8a8784;
    --leaf: #669933;
    --paper: #ffffff;
    --text-light: #ffffff;
  }
  html, body {
    margin: 0;
    padding: 0;
    width: 1200px;
    height: 754px;
    overflow: hidden;
    background: var(--paper);
  }
  .infographic {
    position: relative;
    width: 1200px;
    height: 754px;
    font-family: "Montserrat", sans-serif;
  }
  .shapes {
    position: absolute;
    inset: 0;
  }
  .stat-number {
    position: absolute;
    font-family: "Oswald", sans-serif;
    font-weight: 600;
    color: var(--leaf);
    text-align: center;
    line-height: 1;
    letter-spacing: -1px;
  }
  .stat-label {
    position: absolute;
    color: var(--text-light);
    text-align: center;
    font-weight: 500;
    letter-spacing: 0.5px;
  }
  .headline .stat-number { left: 374px; width: 453px; top: 168px; font-size: 74px; }
  .headline .stat-label { left: 374px; width: 453px; top: 244px; font-size: 26px; line-height: 33px; }
  .ring .stat-number { width: 280px; top: 424px; font-size: 74px; }
  .ring .stat-label { width: 280px; top: 508px; font-size: 25px; line-height: 32.5px; }
  .ring-posting > * { left: 38px; }
  .ring-lurkers > * { left: 460px; }
  .ring-future > * { left: 884px; }
  .source {
    position: absolute;
    left: 188px;
    top: 704px;
    font-size: 24px;
    font-weight: 600;
    color: var(--ink);
    letter-spacing: 0.3px;
  }
  .copyright {
    position: absolute;
    left: 1084px;
    top: 704px;
    font-size: 24px;
    font-weight: 600;
    color: var(--ink);
  }
</style>
</head>
<body>
<main class="infographic">
  <svg class="shapes" width="1200" height="754" viewBox="0 0 1200 754" aria-hidden="false">
    <!-- frame -->
    <rect x="5" y="5" width="1190" height="744" rx="14" fill="none" stroke="var(--ink)" stroke-width="5"/>

    <!-- executive icon row -->
    <g class="executive-row">
      <rect x="20" y="28" width="86" height="90" rx="8" fill="var(--ink)" role="img" aria-label="Executive at laptop icon, user"/>
      <rect x="118" y="28" width="86" height="90" rx="8" fill="var(--ink)" role="img" aria-label="Executive at laptop icon, user"/>
      <rect x="215" y="28" width="86" height="90" rx="8" fill="var(--stone)" role="img" aria-label="Executive at laptop icon"/>
      <rect x="313" y="28" width="86" height="90" rx="8" fill="var(--stone)" role="img" aria-label="Executive at laptop icon"/>
      <rect x="411" y="28" width="86" height="90" rx="8" fill="var(--stone)" role="img" aria-label="Executive at laptop icon"/>
      <rect x="508" y="28" width="86" height="90" rx="8" fill="var(--stone)" role="img" aria-label="Executive at laptop icon"/>
      <rect x="606" y="28" width="86" height="90" rx="8" fill="var(--stone)" role="img" aria-label="Executive at laptop icon"/>
      <rect x="703" y="28" width="86" height="90" rx="8" fill="var(--stone)" role="img" aria-label="Executive at laptop icon"/>
      <rect x="801" y="28" width="86" height="90" rx="8" fill="var(--stone)" role="img" aria-label="Executive at laptop icon"/>
      <rect x="899" y="28" width="86" height="90" rx="8" fill="var(--stone)" role="img" aria-label="Executive at laptop icon"/>
      <rect x="996" y="28" width="86" height="90" rx="8" fill="var(--ink)" role="img" aria-label="Executive at laptop icon, user"/>
      <rect x="1094" y="28" width="86" height="90" rx="8" fill="var(--ink)" role="img" aria-label="Executive at laptop icon, user"/>
    </g>

    <!-- connectors -->
    <g class="connectors" fill="none" stroke="var(--ink)" stroke-width="9" stroke-linejoin="round">
      <path d="M370 236 H186 Q180 236 180 242 V366"/>
      <path d="M832 236 H1018 Q1024 236 1024 242 V366"/>
      <path d="M600 330 V366"/>
    </g>

    <!-- headline box -->
    <rect x="362" y="136" width="478" height="200" rx="10" fill="var(--stone)"/>
    <rect x="374" y="149" width="453" height="176" rx="7" fill="var(--ink)"/>

    <!-- stat rings: r 150.5, circumference 945.6 -->
    <g class="rings" fill="none" stroke-width="19">
      <circle cx="178" cy="522" r="150.5" stroke="var(--stone)"/>
      <circle cx="178" cy="522" r="150.5" stroke="var(--leaf)" stroke-dasharray="661.9 945.6" transform="rotate(-90 178 522)"/>
      <circle cx="600" cy="522" r="150.5" stroke="var(--stone)"/>
      <circle cx="600" cy="522" r="150.5" stroke="var(--leaf)" stroke-dasharray="122.9 945.6" transform="rotate(-90 600 522)"/>
      <circle cx="1024" cy="522" r="150.5" stroke="var(--stone)"/>
      <circle cx="1024" cy="522" r="150.5" stroke="var(--leaf)" stroke-dasharray="378.2 945.6" transform="rotate(-90 1024 522)"/>
    </g>
    <g class="ring-cores" fill="var(--ink)">
      <circle cx="178" cy="522" r="141"/>
      <circle cx="600" cy="522" r="141"/>
      <circle cx="1024" cy="522" r="141"/>
    </g>
  </svg>

  <section class="headline">
    <div class="stat-number">66%</div>
    <p class="stat-label" style="margin:0">of C-Suite Executives use social media for professional purpose</p>
  </section>

  <section class="ring ring-posting">
    <div class="stat-number">70%</div>
    <p class="stat-label" style="margin:0">post original<br>content on a daily/<br>weekly basis</p>
  </section>

  <section class="ring ring-lurkers">
    <div class="stat-number">13%</div>
    <p class="stat-label" style="margin:0">of professional<br>users are<br>lurkers</p>
  </section>

  <section class="ring ring-future">
    <div class="stat-number">40%</div>
    <p class="stat-label" style="margin:0">plan to use social<br>media even more<br>in the future</p>
  </section>

  <p class="source" style="margin:0">Source: 2017 Venmoor Partners Executive Social Media Study</p>
  <p class="copyright" style="margin:0">©2017</p>
</main>
</body>
</html>
```